Business card design needed

Chasing a very simplistic modern design with a logo incorporating "TRV".
I'm starting a plumbing business.
I do water, sanitary and drainage plumbing that will cover residential, commercial, rental, rural, excavation, new housing and all maintanence requirements.

Industry/Entity Type

Business

Contact Information for Business Card

TRV PLUMBING SERVICES
DEAN HOLLOWBY - LICENSED PLUMBER
PHONE: 0481926574
E-MAIL: hollodt7@wirelane.com
NORTHERN SUBURBS

Requirements
Must have
• lower case email address

```html
<!DOCTYPE html>
<html lang="en">
<head>
<meta charset="utf-8">
<title>TRV Plumbing Services — Business Card</title>
<link rel="stylesheet" href="https://fonts.googleapis.com/css2?family=Questrial&display=swap">
<style>
  :root {
    --card-bg: #ffffff;
    --ink: #111111;
    --ink-muted: #6b6b6b;
  }
  html, body {
    margin: 0;
    padding: 0;
    width: 1200px;
    height: 689px;
    overflow: hidden;
    background: var(--card-bg);
  }
  .card {
    position: relative;
    width: 1200px;
    height: 689px;
    background: var(--card-bg);
    color: var(--ink);
    font-family: "Questrial", sans-serif;
    font-weight: 400;
    overflow: hidden;
  }
  .brand__name {
    position: absolute;
    left: 58px;
    top: 18px;
    margin: 0;
    font-size: 230px;
    line-height: 1;
    letter-spacing: 12px;
    color: var(--ink);
    white-space: nowrap;
  }
  .brand__tagline {
    position: absolute;
    left: 60px;
    top: 240px;
    margin: 0;
    font-size: 44px;
    line-height: 1;
    letter-spacing: 1px;
    font-variant: small-caps;
    white-space: nowrap;
  }
  .contact {
    position: absolute;
    right: 63px;
    top: 0;
    text-align: right;
    white-space: nowrap;
  }
  .contact__name,
  .contact__role {
    position: absolute;
    right: 0;
    margin: 0;
    line-height: 1;
    font-variant: small-caps;
    letter-spacing: 1.5px;
  }
  .contact__name {
    top: 328px;
    font-size: 58px;
    color: var(--ink);
  }
  .contact__role {
    top: 385px;
    font-size: 52px;
    color: var(--ink-muted);
  }
  .contact__details {
    position: absolute;
    right: 0;
    top: 491px;
    list-style: none;
    margin: 0;
    padding: 0;
    font-size: 40px;
    line-height: 50.5px;
    letter-spacing: 1px;
  }
  .contact__email-address {
    text-transform: none;
    font-variant: normal;
  }
</style>
</head>
<body>
  <main class="card">
    <header class="brand">
      <p class="brand__name">TRV</p>
      <p class="brand__tagline">Plumbing Services</p>
    </header>
    <section class="contact">
      <h1 class="contact__name">Dean Hollowby</h1>
      <p class="contact__role">Licensed Plumber</p>
      <ul class="contact__details">
        <li class="contact__phone">PHONE: 0481926574</li>
        <li class="contact__email">E-MAIL: <span class="contact__email-address">hollodt7@wirelane.com</span></li>
        <li class="contact__area">NORTHERN SUBURBS</li>
      </ul>
    </section>
  </main>
</body>
</html>
```